Nice, modern, and professional credit repair website

We're a new credit repair company and we need a website to inform our prospective clients about the service we provide. We wan't it to catch the attention of the people as well as it be informative of the different types of derogatory items that can be listed on a report. Please refer to ( www.pathtoprime.example ) for an idea of what I'm looking for.

Colors
0455a3
0293ce
33a6d7
ffffff

Requirements
Must have
• The website must include information regarding credit repair. We'd like the website to include modern colors similar to that of our logo.
A link to our Facebook page. Www.facebook.com/brevantaledgerpartners
A link to our Instagram page: @BrevantaLedgerPartners
A link to our Snapchat page: Brevanta-Ledger
Also, we'd like to have an area where clients would fill out basic information where we could reach out to them.
Nice to have
• Images of new homes, cars, credit cards (Should NOT endorse Quilo, TF, BRONT, or Palvenry.)

```html
<!DOCTYPE html>
<html lang="en">
<head>
<meta charset="utf-8">
<title>Brevanta Ledger Partners – Credit Repair</title>
<link rel="stylesheet" href="https://fonts.googleapis.com/css2?family=Montserrat:wght@400;600;700;800;900&family=Open+Sans:wght@400;600;700&family=Bebas+Neue&display=swap">
<style>
:root{
  --blue:#0b4f9c;
  --blue-deep:#083d7c;
  --blue-mid:#0455a3;
  --sky:#2a7fd0;
  --yellow:#f6c22c;
  --yellow-deep:#d9a21a;
  --banner:#f7e23c;
  --ink:#2a2a2a;
  --grey:#555;
  --line:#d5d9e0;
  --dark:#161616;
  --white:#ffffff;
}
html,body{margin:0;padding:0;overflow:hidden;background:var(--white);}
.canvas{position:relative;width:1200px;height:4120px;overflow:hidden;font-family:"Open Sans",Arial,sans-serif;color:var(--ink);}
.backdrop{position:absolute;left:0;top:0;}
.abs{position:absolute;margin:0;}

/* header */
.top-strip{left:0;top:0;width:1200px;height:5px;background:var(--blue);}
.brand{left:75px;top:48px;display:flex;align-items:center;gap:10px;}
.brand-dot{width:50px;height:50px;border-radius:50%;border:3px solid var(--blue);box-sizing:border-box;}
.brand-name{font-family:"Montserrat",sans-serif;font-weight:700;color:var(--blue);line-height:1;}
.brand-name .l1{display:block;font-size:25px;letter-spacing:1px;}
.brand-name .l2{display:block;font-size:10px;letter-spacing:3px;margin-top:4px;}
.util{top:18px;font-size:12px;font-family:"Montserrat",sans-serif;color:var(--blue);font-weight:600;display:flex;align-items:center;gap:6px;}
.search-box{left:693px;top:17px;width:180px;height:18px;border:1.5px solid var(--blue);border-radius:10px;}
.login-tab{left:890px;top:0;width:115px;height:36px;background:var(--blue-deep);clip-path:polygon(0 0,100% 0,82% 100%,0 100%);color:var(--white);font-size:12px;font-family:"Montserrat",sans-serif;font-weight:600;display:flex;align-items:center;padding-left:22px;box-sizing:border-box;gap:6px;}
.socials{display:flex;gap:5px;}
.socials span{width:16px;height:16px;border-radius:50%;background:var(--blue);display:block;}
.nav{left:475px;top:66px;display:flex;gap:21px;font-family:"Montserrat",sans-serif;font-size:12.5px;font-weight:500;color:var(--ink);}
.nav a{color:inherit;text-decoration:none;padding:3px 4px;}
.nav a.active{background:var(--blue);color:var(--white);border-radius:3px;font-weight:700;}

/* hero */
.hero-title{left:70px;top:380px;font-family:"Montserrat",sans-serif;font-weight:900;font-size:98px;color:var(--yellow);letter-spacing:2px;line-height:1;}
.hero-sub{left:72px;top:488px;font-family:"Montserrat",sans-serif;font-size:25px;color:var(--white);line-height:33px;letter-spacing:.3px;}
.pill{left:70px;top:562px;padding:5px 16px;border:2px solid var(--yellow);background:var(--yellow-deep);border-radius:20px;color:var(--white);font-family:"Montserrat",sans-serif;font-size:19px;}

/* section titles */
.sec-title{left:0;width:1200px;display:flex;justify-content:center;align-items:center;gap:18px;font-family:"Montserrat",sans-serif;font-weight:900;font-size:45px;letter-spacing:.5px;}
.sec-title .mark{width:56px;height:56px;border-radius:50%;border:4px solid currentColor;box-sizing:border-box;}
.sec-title.on-white{color:var(--blue);}
.sec-title.on-white .dark{color:var(--ink);}
.sec-title.on-blue{color:var(--white);}
.rule{width:64px;height:3px;left:568px;}
.rule.blue{background:var(--blue);}
.rule.white{background:var(--white);}

/* about */
.about-photo{left:128px;top:1019px;width:331px;height:242px;background:linear-gradient(135deg,#6b7380,#b9bec6 55%,#e0dcd4);}
.about-copy{left:494px;top:1014px;width:566px;font-size:11.5px;line-height:15px;color:var(--grey);}
.about-copy h3{margin:0 0 4px;font-size:19px;color:var(--blue);font-weight:700;line-height:24px;}
.about-copy p{margin:0 0 14px;}
.btn-small{display:inline-flex;align-items:center;gap:14px;background:var(--blue);color:var(--white);font-size:10px;padding:4px 8px;border-radius:4px;font-family:"Montserrat",sans-serif;}

/* services */
.svc-intro{left:100px;top:1640px;width:1000px;text-align:center;color:var(--white);font-size:12.5px;line-height:16px;}
.svc{width:175px;color:var(--white);}
.svc h4{margin:0;font-family:"Montserrat",sans-serif;font-size:17px;font-weight:700;line-height:20px;}
.svc p{margin:2px 0 0;font-size:8px;line-height:9.5px;}
.svc.right-al{text-align:right;}

/* faq */
.faq{width:519px;height:45px;border:1.5px solid var(--line);box-sizing:border-box;box-shadow:0 1px 3px rgba(0,0,0,.08);display:flex;align-items:center;justify-content:space-between;padding:0 14px 0 16px;font-family:"Montserrat",sans-serif;font-size:17px;color:var(--ink);background:var(--white);}
.faq b{color:var(--sky);font-weight:500;}
.faq i{font-style:normal;font-size:20px;color:var(--grey);}
.faq-open{left:619px;top:2570px;width:519px;height:251px;background:var(--blue);color:var(--white);padding:18px 22px;box-sizing:border-box;}
.faq-open .q{display:flex;justify-content:space-between;font-family:"Montserrat",sans-serif;font-size:17px;margin-bottom:14px;}
.faq-open p{margin:0;font-size:13px;line-height:27px;text-align:justify;}

/* banner */
.banner-frame{left:11px;top:3075px;width:1176px;height:264px;border:2px solid var(--blue);box-sizing:border-box;}
.banner-title{left:486px;top:3120px;font-family:"Bebas Neue",sans-serif;font-size:118px;line-height:1;color:var(--blue);letter-spacing:3px;}
.banner-sub{left:490px;top:3228px;font-family:"Montserrat",sans-serif;font-size:26px;color:var(--ink);letter-spacing:1px;}
.banner-btn{left:585px;top:3275px;display:flex;align-items:center;gap:10px;}
.banner-btn .ln{width:30px;height:1.5px;background:var(--ink);}
.banner-btn span.txt{background:var(--yellow-deep);border-radius:14px;padding:3px 12px;font-size:13px;font-family:"Montserrat",sans-serif;color:var(--ink);}

/* testimonial */
.quote{left:300px;top:3532px;width:600px;text-align:center;font-size:12.5px;line-height:20px;color:var(--grey);}
.quote .qm{color:var(--blue);font-size:30px;font-weight:700;font-family:Georgia,serif;line-height:0;vertical-align:-10px;}
.client{left:0;width:1200px;top:3612px;text-align:center;}
.client strong{display:block;color:var(--blue);font-family:"Montserrat",sans-serif;font-size:15px;font-weight:600;}
.client span{font-size:10.5px;color:var(--grey);}

/* footer */
.f-brand{left:75px;top:3852px;}
.f-brand .brand-dot{border-color:var(--blue);}
.f-about{left:77px;top:3916px;width:250px;font-size:11px;line-height:15px;color:var(--white);text-align:justify;}
.f-more{left:77px;top:3997px;}
.f-head{font-family:"Montserrat",sans-serif;font-size:17px;color:var(--blue);font-weight:600;padding-bottom:10px;border-bottom:1.5px dotted #555;width:160px;letter-spacing:.5px;}
.f-col{top:3848px;color:var(--white);}
.f-col ul{list-style:none;margin:14px 0 0;padding:0;font-size:14px;line-height:26.5px;}
.f-col ul li::before{content:"› ";color:#888;}
.f-contact{font-size:11.5px;line-height:22px;margin-top:12px;}
.f-contact div{display:flex;align-items:center;gap:8px;}
.f-contact .ic{width:8px;height:8px;background:var(--blue);display:inline-block;}
.divider{width:0;border-left:1.5px dotted #555;top:3875px;height:150px;}
.f-soc{display:flex;gap:18px;margin-top:14px;}
.f-soc span{width:12px;height:12px;border-radius:50%;background:var(--blue);display:block;}
.f-phone{font-family:"Montserrat",sans-serif;font-size:20px;font-weight:700;color:var(--white);}
.bottom-bar{left:0;top:4064px;width:1200px;height:56px;background:var(--blue);color:var(--white);font-size:13.5px;display:flex;align-items:center;justify-content:center;}
</style>
</head>
<body>
<div class="canvas">

<svg class="backdrop" width="1200" height="4120" viewBox="0 0 1200 4120" aria-hidden="false">
  <defs>
    <linearGradient id="gradGrad" x1="0" y1="0" x2="1" y2="1">
      <stop offset="0" stop-color="#2b2f3a"/><stop offset=".5" stop-color="#5a4a3e"/><stop offset="1" stop-color="#1e2530"/>
    </linearGradient>
    <linearGradient id="bannerPhoto" x1="0" y1="0" x2="1" y2="0">
      <stop offset="0" stop-color="#cdb82c"/><stop offset=".6" stop-color="#e9d438"/><stop offset="1" stop-color="#f7e23c"/>
    </linearGradient>
  </defs>
  <!-- hero -->
  <path d="M0 858 L688 818 L1140 640" fill="none" stroke="#f6c22c" stroke-width="20"/>
  <polygon points="1188,612 1110,612 1165,672" fill="#f6c22c"/>
  <polygon points="0,140 1200,140 1200,598 688,806 0,846" fill="#0b4f9c"/>
  <g role="img" aria-label="Photo of a smiling graduate in cap and gown holding a diploma">
    <polygon points="690,250 880,165 1200,165 1200,598 688,806 560,700" fill="url(#gradGrad)"/>
  </g>
  <!-- services band -->
  <polygon points="0,1475 451,1331 1200,1410 1200,2216 688,2379 0,2416" fill="#0b4f9c"/>
  <!-- banner -->
  <rect x="0" y="3064" width="1200" height="285" fill="#f7e23c"/>
  <g role="img" aria-label="Photo of a happy man at the wheel of a new car, tinted yellow">
    <rect x="0" y="3064" width="520" height="285" fill="url(#bannerPhoto)"/>
  </g>
  <!-- footer -->
  <polygon points="0,3848 688,3806 1200,3606 1200,4120 0,4120" fill="#161616"/>
  <path d="M0 3838 L688 3796 L1140 3620" fill="none" stroke="#f6c22c" stroke-width="20"/>
  <polygon points="1188,3592 1110,3592 1165,3652" fill="#f6c22c"/>

  <!-- services diagram -->
  <circle cx="597" cy="1968" r="184" fill="none" stroke="#fff" stroke-width="2.5"/>
  <circle cx="597" cy="1968" r="96" fill="#fff"/>
  <circle cx="597" cy="1968" r="80" fill="none" stroke="#0b4f9c" stroke-width="6"/>
  <g fill="#fff">
    <circle cx="528" cy="1797" r="38"/><circle cx="677" cy="1797" r="38"/>
    <circle cx="429" cy="1890" r="38"/><circle cx="765" cy="1890" r="38"/>
    <circle cx="429" cy="2032" r="38"/><circle cx="765" cy="2032" r="38"/>
    <circle cx="528" cy="2139" r="38"/><circle cx="677" cy="2139" r="38"/>
  </g>
  <g fill="#0b4f9c" stroke="none">
    <!-- bankruptcies: coin -->
    <circle cx="528" cy="1797" r="18"/><text x="528" y="1805" text-anchor="middle" font-family="Montserrat" font-weight="800" font-size="22" fill="#fff">$</text>
    <!-- late payments: card -->
    <rect x="657" y="1784" width="40" height="26" rx="4"/><rect x="657" y="1790" width="40" height="5" fill="#fff"/>
    <!-- child support: heart -->
    <path d="M429 1910 L410 1890 A10 10 0 0 1 429 1878 A10 10 0 0 1 448 1890 Z"/>
    <!-- charge-offs: document -->
    <rect x="748" y="1874" width="34" height="32" rx="3"/><g fill="#fff"><rect x="754" y="1881" width="22" height="3"/><rect x="754" y="1888" width="22" height="3"/><rect x="754" y="1895" width="14" height="3"/></g>
    <!-- foreclosures: house -->
    <polygon points="409,2032 429,2014 449,2032"/><rect x="414" y="2032" width="30" height="18"/>
    <!-- repossessions: car -->
    <rect x="745" y="2026" width="40" height="14" rx="4"/><polygon points="753,2026 760,2015 772,2015 779,2026"/><circle cx="755" cy="2042" r="5"/><circle cx="775" cy="2042" r="5"/>
    <!-- student loans: cap -->
    <polygon points="505,2133 528,2123 551,2133 528,2143"/><rect x="516" y="2138" width="24" height="11"/>
    <!-- hospital bills: clipboard -->
    <rect x="662" y="2120" width="30" height="38" rx="3"/><rect x="670" y="2116" width="14" height="7" rx="2"/><g fill="#fff"><rect x="668" y="2132" width="18" height="3"/><rect x="668" y="2140" width="18" height="3"/></g>
  </g>
  <!-- testimonial arrows -->
  <polyline points="105,3528 82,3552 105,3576" fill="none" stroke="#bbb" stroke-width="4"/>
  <polyline points="1080,3528 1103,3552 1080,3576" fill="none" stroke="#bbb" stroke-width="4"/>
</svg>

<!-- header -->
<div class="abs top-strip"></div>
<div class="abs brand">
  <span class="brand-dot"></span>
  <span class="brand-name"><span class="l1">BREVANTA</span><span class="l2">LEDGER PARTNERS</span></span>
</div>
<div class="abs util" style="left:478px;">
  <svg width="12" height="12" viewBox="0 0 12 12"><path d="M2 1 L5 1 L6 4 L4.5 5.5 A7 7 0 0 0 6.5 7.5 L8 6 L11 7 L11 10 Q5 11 1 4 Z" fill="#0b4f9c"/></svg>
  <span style="color:#2a2a2a;font-weight:500">+1 555-014-2290</span>
</div>
<div class="abs util" style="left:630px;">SEARCH</div>
<div class="abs search-box"></div>
<svg class="abs" style="left:853px;top:20px" width="14" height="14" viewBox="0 0 14 14"><circle cx="6" cy="6" r="4" fill="none" stroke="#0b4f9c" stroke-width="2"/><line x1="9" y1="9" x2="13" y2="13" stroke="#0b4f9c" stroke-width="2"/></svg>
<div class="abs login-tab">
  <svg width="13" height="13" viewBox="0 0 13 13"><circle cx="6.5" cy="4" r="3.2" fill="#fff"/><path d="M0.5 13 Q6.5 4 12.5 13 Z" fill="#fff"/></svg>LOGIN
</div>
<div class="abs socials" style="left:1023px;top:17px;"><span></span><span></span><span></span></div>
<nav class="abs nav">
  <a class="active" href="#">HOME</a><a href="#">ABOUT</a><a href="#">TEAM</a><a href="#">INVESTMENTS</a><a href="#">PORTFOLIO COMPANIES</a><a href="#">PRESS</a><a href="#">CONTACT US</a>
</nav>

<!-- hero -->
<h1 class="abs hero-title">SIGN UP</h1>
<p class="abs hero-sub">FOR OUR CREDIT REPORT REPAIRING<br>AND IMPROVE YOUR LENDING LIMITS.</p>
<div class="abs pill">Schedule Your Credit Analusis &amp; Consultation</div>

<!-- about -->
<h2 class="abs sec-title on-white" style="top:882px;"><span class="mark"></span>ABOUT US</h2>
<div class="abs rule blue" style="top:960px;"></div>
<div class="abs about-photo" role="img" aria-label="Photo of a hand passing car keys into another hand"></div>
<div class="abs about-copy">
  <h3>We specialize in repairing credit reports made easy.</h3>
  <p>It's our passion. When you sign up today, you can start seeing results in as little as 45 days. We're ready to answer any questions you may have.</p>
  <p>Lorem ipsum dolor sit amet, consectetur adipiscing elit, sed do eiusmod tempor incididunt ut labore et dolore magna aliqua. Ut enim ad minim veniam, quis nostrud exercitation ullamco laboris nisi</p>
  <p>ut aliquip ex ea commodo consequat. Duis aute irure dolor in reprehenderit in voluptate velit esse cillum dolore eu fugiat nulla pariatur. Ut enim ad minim veniam, quis nostrud exercitation ullamco laboris nisi&nbsp; Duis aute irure dolor in reprehenderit in voluptate velit esse cillum dolore eu fugiat nulla pariatur. Ut enim ad minim veniam, quis nostrud exercitation ullamco laboris nisi quis nostrud exercitation ullamco laboris nisi</p>
  <span class="btn-small">READ MORE <span>›</span></span>
</div>

<!-- services -->
<h2 class="abs sec-title on-blue" style="top:1522px;"><span class="mark"></span>OUR SERVICES</h2>
<div class="abs rule white" style="top:1598px;"></div>
<p class="abs svc-intro">Lorem ipsum dolor sit amet, consectetur adipiscing elit, sed do eiusmod tempor incididunt ut labore et dolore magna aliqua. Ut enim ad minim veniam, quis nostrud exercitation ullamco laboris nisi&nbsp; ut aliquip ex ea commodo consequat. Duis aute irure dolor in reprehenderit in voluptate velit esse cillum dolore eu fugiat nulla pariatur. Excepteur sint occaecat cupidatat non proident, sunt in culpa qui officia deserunt mollit anim id est laborum</p>

<div class="abs svc right-al" style="left:305px;top:1756px;"><h4>Bankruptcies</h4><p>Lorem ipsum dolor sit amet, consectetur adipiscing elit, sed do eiusmod tempor incididunt ut labore et dolore magna aliqua.</p></div>
<div class="abs svc" style="left:728px;top:1760px;"><h4>Late Payments</h4><p>Lorem ipsum dolor sit amet, consectetur adipiscing elit, sed do eiusmod tempor incididunt ut labore et dolore magna aliqua.</p></div>
<div class="abs svc right-al" style="left:209px;top:1858px;"><h4>Child Support</h4><p>Lorem ipsum dolor sit amet, consectetur adipiscing elit, sed do eiusmod tempor incididunt ut labore et dolore magna aliqua.</p></div>
<div class="abs svc" style="left:818px;top:1862px;"><h4>Charge-Offs</h4><p>Lorem ipsum dolor sit amet, consectetur adipiscing elit, sed do eiusmod tempor incididunt ut labore et dolore magna aliqua.</p></div>
<div class="abs svc right-al" style="left:209px;top:2003px;"><h4>Foreclosures</h4><p>Lorem ipsum dolor sit amet, consectetur adipiscing elit, sed do eiusmod tempor incididunt ut labore et dolore magna aliqua.</p></div>
<div class="abs svc" style="left:818px;top:2005px;"><h4>Reposessions</h4><p>Lorem ipsum dolor sit amet, consectetur adipiscing elit, sed do eiusmod tempor incididunt ut labore et dolore magna aliqua.</p></div>
<div class="abs svc right-al" style="left:305px;top:2124px;"><h4>Student Loans</h4><p>Lorem ipsum dolor sit amet, consectetur adipiscing elit, sed do eiusmod tempor incididunt ut labore et dolore magna aliqua.</p></div>
<div class="abs svc" style="left:728px;top:2130px;"><h4>Hospital Bills</h4><p>Lorem ipsum dolor sit amet, consectetur adipiscing elit, sed do eiusmod tempor incididunt ut labore et dolore magna aliqua.</p></div>

<!-- faq -->
<h2 class="abs sec-title on-white" style="top:2442px;"><span class="mark"></span>FREQUENTLY ASKED <span class="dark">QUESTIONS</span></h2>
<div class="abs rule blue" style="top:2516px;"></div>
<div class="abs faq" style="left:59px;top:2572px;"><span><b>Q: 1</b> LOREMIPSUM IS SIMPLY DUMMY TEXT?</span><i>+</i></div>
<div class="abs faq" style="left:59px;top:2670px;"><span><b>Q: 2</b> LOREMIPSUM IS SIMPLY DUMMY TEXT?</span><i>+</i></div>
<div class="abs faq" style="left:59px;top:2763px;"><span><b>Q: 3</b> LOREMIPSUM IS SIMPLY DUMMY TEXT?</span><i>+</i></div>
<div class="abs faq" style="left:59px;top:2852px;"><span><b>Q: 4</b> LOREMIPSUM IS SIMPLY DUMMY TEXT?</span><i>+</i></div>
<div class="abs faq" style="left:59px;top:2945px;"><span><b>Q: 5</b> LOREMIPSUM IS SIMPLY DUMMY TEXT?</span><i>+</i></div>
<div class="abs faq-open">
  <div class="q"><span>Q: 6LOREMIPSUM IS SIMPLY DUMMY TEXT?</span><span>-</span></div>
  <p>Lorem ipsum dolor sit amet, consectetur adipiscing elit. Quid autem habent admirationis, cum prope accesseris? An hoc usque quaque, aliter in vita? Non igitur de improbo, sed de callido improbo quaerimus, qualis Q. Nam quibus rebus efficiunturvoluptates, eae non sunt in potestate sapientis. Negare non possum. Huic mori optimum esse propter</p>
</div>
<div class="abs faq" style="left:619px;top:2852px;"><span><b>Q: 7</b> LOREMIPSUM IS SIMPLY DUMMY TEXT?</span><i>+</i></div>
<div class="abs faq" style="left:619px;top:2945px;"><span><b>Q: 8</b> LOREMIPSUM IS SIMPLY DUMMY TEXT?</span><i>+</i></div>

<!-- banner -->
<div class="abs banner-frame"></div>
<h2 class="abs banner-title">SEARCHING FOR</h2>
<p class="abs banner-sub">A FIRST - CLASS CREDIT REPAIR COMPANY</p>
<div class="abs banner-btn"><span class="ln"></span><span class="txt">Schedule Your Credit Analusis &amp; Consultation</span><span class="ln"></span></div>

<!-- testimonials -->
<h2 class="abs sec-title on-white" style="top:3432px;"><span class="mark"></span>CLIENT <span class="dark">TESTIMONIALS</span></h2>
<p class="abs quote"><span class="qm">“</span> Lorem ipsum dolor sit amet, consectetur adipiscing elit. Quid autem habent admirationis, cum prope accesseris?An hoc usque quaque, aliter in vita? Non igitur de improbo, sed de callidoim-probo quaerimus, qualis Q. Nam quibus rebus efficiunturvoluptates. <span class="qm">”</span></p>
<div class="abs client"><strong>MARCUS DELVANE</strong><span>Regional Administration Director</span></div>

<!-- footer -->
<div class="abs brand f-brand">
  <span class="brand-dot"></span>
  <span class="brand-name"><span class="l1">BREVANTA</span><span class="l2">LEDGER PARTNERS</span></span>
</div>
<p class="abs f-about">Lorem ipsum dolor sit amet, consectetur adipiscing elit. Quid autem habent admirationis, cum prope accesseris? An hoc usque quaque, aliter in vita?</p>
<span class="abs btn-small f-more">READ MORE <span>›</span></span>

<div class="abs divider" style="left:368px;"></div>
<div class="abs f-col" style="left:419px;">
  <div class="f-head">QUICK LINKS</div>
  <ul><li>Home</li><li>About us</li><li>Services</li><li>Customer Support</li><li>Contact us</li></ul>
</div>
<div class="abs divider" style="left:608px;"></div>
<div class="abs f-col" style="left:651px;">
  <div class="f-head">CONTACT</div>
  <div class="f-contact">
    <div style="line-height:15px;display:block;margin-bottom:8px;">4417 Harlow Lane<br>Fenmoor, IL 60900</div>
    <div><span class="ic"></span>+1 555-014-2290</div>
    <div><span class="ic"></span>+1 555-014-3371</div>
    <div><span class="ic"></span>hello@brevantaledger.example</div>
    <div><span class="ic"></span>www.brevantaledger.example</div>
  </div>
</div>
<div class="abs divider" style="left:902px;"></div>
<div class="abs f-col" style="left:946px;">
  <div class="f-head">FOLLOW US ON</div>
  <div class="f-soc"><span></span><span></span><span></span><span></span></div>
  <div style="width:18px;height:1.5px;background:#fff;margin:34px 0 20px;"></div>
  <div class="f-head" style="border:none;padding:0;">CALL US ON</div>
  <div class="f-phone">+1 555-014-2290</div>
</div>

<div class="abs bottom-bar">© 2020 Brevanta Ledger Partners &nbsp;|&nbsp; Privacy Policy &nbsp;|&nbsp; User Agreement</div>

</div>
</body>
</html>
```